Brent's Business Cards

My husband is a self employed Cabinet Maker... who contracts to Building companies and clients directly.
He installs kitchesn, designs and also completes renovations and building work.

I would like a small, FUNKY, simple but eye catching design.

It needs to incorporate the following.
Custom Cabinets / Installations / Renovations / Design

Commercial and Residential

He does not have a Website or Facebook,
contact number is 0438 207 964 and email is brentkelway@mailpost.example

I would like a Grey/Silver on black, or blue covering.. I am open to colour designs?

Thank you. :-)

Target Market(s)

Building Companies
Clients
Other Trades people onsite,. to give out at job sites

Industry/Entity Type

Business

Contact Information for Business Card

Phone: 0438 207 964
Email: brentkelway@mailpost.example

Font styles to use
Sans Serif

Colors
0592cd
747474
474747
1b1b1b
85cae6

Requirements
Must have
• Funky, simple, eye catching design
• Would like use of Silver/Grey - and a colour that would complement this.
• Am open to ideas :-)
Nice to have
• We do not have a logo or picture, will leave this up to you if you think an image would be beneficial???
• Thank you.

Files

```html
<!DOCTYPE html>
<html lang="en">
<head>
<meta charset="utf-8">
<title>Brent Kelway – Business Card</title>
<link rel="stylesheet" href="https://fonts.googleapis.com/css2?family=Lato:wght@400;700;900&display=swap">
<style>
  :root {
    --page-bg: #474747;
    --band: #0b0b0d;
    --text-light: #ffffff;
    --blue-deep: #0a1f66;
    --blue-mid: #1f4fc4;
    --blue-bright: #5d8fe6;
    --blue-glow: #a9c8f5;
    --blue-accent: #0592cd;
  }
  html, body {
    margin: 0;
    padding: 0;
    width: 1200px;
    height: 900px;
    overflow: hidden;
    background: var(--page-bg);
    font-family: "Lato", sans-serif;
  }
  .card {
    position: absolute;
    left: 100px;
    top: 144px;
    width: 1000px;
    height: 611px;
    border-radius: 26px;
    overflow: hidden;
    background: var(--blue-deep);
  }
  .card__backdrop {
    position: absolute;
    inset: 0;
    background:
      radial-gradient(ellipse 55% 60% at 48% 38%, var(--blue-glow) 0%, var(--blue-bright) 35%, transparent 75%),
      linear-gradient(100deg, var(--blue-deep) 0%, var(--blue-mid) 30%, var(--blue-mid) 70%, var(--blue-deep) 100%);
  }
  .band {
    position: absolute;
    left: 0;
    background: var(--band);
    color: var(--text-light);
  }
  .name-band {
    top: 112px;
    width: 450px;
    height: 82px;
    display: flex;
    align-items: center;
    padding-left: 44px;
    box-sizing: border-box;
    font-size: 50px;
    font-weight: 400;
    letter-spacing: 0.5px;
  }
  .name-band strong { font-weight: 700; margin-left: 12px; }
  .contact-band {
    height: 36px;
    display: flex;
    align-items: center;
    padding-left: 44px;
    box-sizing: border-box;
    font-size: 24px;
  }
  .contact-band--phone { top: 268px; width: 320px; }
  .contact-band--email { top: 308px; width: 470px; }
  .services-band {
    top: 392px;
    width: 100%;
    height: 142px;
    display: flex;
    flex-direction: column;
    justify-content: center;
    align-items: flex-end;
    padding-right: 40px;
    box-sizing: border-box;
    font-size: 29px;
    font-weight: 700;
    text-transform: uppercase;
    letter-spacing: 0.3px;
    line-height: 1.45;
  }
  .services-band .dot {
    display: inline-block;
    width: 20px;
    height: 20px;
    border-radius: 50%;
    background: var(--text-light);
    margin: 0 14px;
    vertical-align: 2px;
  }
  .services-line--second { font-size: 31px; }
</style>
</head>
<body>
  <div class="card">
    <div class="card__backdrop" role="img" aria-label="Blue square mosaic background with a bright centre glow"></div>
    <div class="band name-band">Brent<strong>Kelway</strong></div>
    <div class="band contact-band contact-band--phone">Phone: 0438 207 964</div>
    <div class="band contact-band contact-band--email">Email: brentkelway@mailpost.example</div>
    <div class="band services-band">
      <div class="services-line">Custom Cabinets<span class="dot"></span>Installations</div>
      <div class="services-line services-line--second">Renovations<span class="dot"></span>Design Commercial and Residential</div>
    </div>
  </div>
</body>
</html>
```